One-Page Flat Design for SEO Company [2 DAYS]

We need a one-page flat design for our SEO company. Our current website is http://www.rankloft.com/. We are looking to completely re-design the site using new flat design techniques.
Below are some examples of the type of style we're going after:
http://quormel.com/
http://tobyrand.co.uk/
https://pentaly.co/
http://milesporter.me/
As you can see- flat, clean, minimal. It is very important you follow this type of style.
For colour scheme, you may use one of the pre-made colour palettes from here:
http://www.vornacle.com/blog/inspiration/24-flat-designs-with-compelling-color-palettes
I've attached a wireframe to be followed.
Hi,

```html
<!DOCTYPE html>
<html lang="en">
<head>
<meta charset="utf-8">
<title>Rankloft — SEO services that actually work</title>
<link rel="stylesheet" href="https://fonts.googleapis.com/css2?family=Montserrat:wght@400;600;700&family=Open+Sans:wght@400;600;700&family=Titillium+Web:wght@300;400;600;700&display=swap">
<style>
  :root {
    --teal: #43c7aa;
    --orange: #fe8a4c;
    --coral: #fd6a5a;
    --navy: #34495e;
    --slate: #8fb3c2;
    --slate-line: #a6c3cf;
    --white: #ffffff;
    --ink: #3b4a58;
    --heading: "Titillium Web", sans-serif;
    --hero: "Montserrat", sans-serif;
    --body: "Open Sans", sans-serif;
  }
  * { box-sizing: border-box; margin: 0; padding: 0; }
  html, body { width: 1200px; height: 3535px; overflow: hidden; }
  body { font-family: var(--body); color: var(--white); background: var(--navy); }
  section, header, footer { position: relative; width: 1200px; }

  /* Hero */
  .hero { height: 392px; overflow: hidden; }
  .hero-photo { position: absolute; inset: 0; background: linear-gradient(100deg, #4b4f55 0%, #7b7a78 35%, #b9b3aa 60%, #5b6068 85%, #3d4248 100%); }
  .hero-shade { position: absolute; inset: 0; background: rgba(20, 28, 38, 0.35); }
  .site-nav { position: absolute; top: 0; left: 0; right: 0; height: 65px; background: rgba(38, 55, 72, 0.85); }
  .brand { position: absolute; left: 206px; top: 18px; font-family: var(--hero); font-weight: 700; font-size: 24px; letter-spacing: 2px; }
  .nav-links { position: absolute; right: 203px; top: 24px; display: flex; gap: 46px; list-style: none; font-family: var(--hero); font-size: 13px; letter-spacing: 0.5px; }
  .hero-copy { position: absolute; left: 206px; top: 98px; }
  .hero-title { font-family: var(--hero); font-weight: 600; font-size: 50px; line-height: 56px; }
  .hero-title strong { font-weight: 700; }
  .hero-lead { margin-top: 12px; font-family: var(--hero); font-weight: 600; font-size: 20px; line-height: 24px; }
  .btn-outline { position: absolute; left: 206px; top: 298px; width: 154px; height: 41px; border: 2px solid var(--white); font-family: var(--hero); font-size: 16px; line-height: 37px; text-align: center; }

  /* Shared */
  .section-title { font-family: var(--heading); font-weight: 300; font-size: 34px; text-align: center; letter-spacing: 1px; }
  .section-title strong { font-weight: 700; }
  .section-sub { font-size: 13px; line-height: 20px; text-align: center; margin-top: 8px; }

  /* Why */
  .why { height: 560px; background: var(--teal); padding-top: 42px; }
  .arrow { position: absolute; top: 240px; }
  .arrow-left { left: 118px; }
  .arrow-right { left: 1052px; }
  .features { position: absolute; top: 240px; left: 0; width: 1200px; }
  .feature { position: absolute; width: 240px; text-align: center; }
  .feature svg { display: block; margin: 0 auto; }
  .feature h3 { margin-top: 70px; font-family: var(--heading); font-weight: 700; font-size: 17px; letter-spacing: 0.5px; }
  .feature p { margin-top: 10px; font-size: 12px; line-height: 16px; padding: 0 40px; }

  /* Plans */
  .plans { height: 664px; background: var(--orange); padding-top: 50px; }
  .plan-table { position: absolute; left: 209px; top: 192px; display: flex; }
  .plan { width: 195px; height: 389px; background: var(--slate); text-align: center; position: relative; }
  .plan + .plan { border-left: 1px solid var(--slate-line); }
  .plan-head { height: 94px; border-bottom: 1px solid var(--slate-line); padding-top: 24px; }
  .plan-name { font-family: var(--heading); font-weight: 700; font-size: 18px; color: var(--ink); letter-spacing: 0.5px; }
  .plan-price { margin-top: 4px; font-size: 13px; color: var(--white); }
  .plan-list { list-style: none; margin-top: 38px; font-size: 13px; line-height: 32px; }
  .plan-btn { position: absolute; left: 50%; bottom: 34px; transform: translateX(-50%); width: 118px; height: 32px; border: 1px solid var(--white); font-size: 12px; line-height: 30px; }
  .plan-featured { background: var(--navy); height: 404px; margin-top: -9px; border-left: none; }
  .plan-featured .plan-head { height: 103px; padding-top: 30px; border-color: #4d6379; }
  .plan-featured .plan-name { color: var(--white); }
  .plan-featured .plan-btn { background: var(--teal); border-color: var(--teal); bottom: 36px; }

  /* Guarantee */
  .guarantee { height: 129px; background: var(--coral); }
  .guarantee-text { position: absolute; left: 256px; top: 40px; font-family: var(--heading); font-weight: 300; font-size: 34px; letter-spacing: 0.5px; }
  .guarantee-text strong { font-weight: 700; }
  .btn-navy { position: absolute; left: 796px; top: 47px; width: 133px; height: 47px; background: var(--navy); font-size: 13px; font-weight: 600; line-height: 47px; text-align: center; }

  /* Services */
  .services { height: 820px; background: var(--navy); padding-top: 45px; }
  .tabs { position: absolute; left: 206px; top: 165px; display: flex; }
  .tab { width: 395px; height: 50px; font-family: var(--heading); font-weight: 700; font-size: 26px; line-height: 50px; text-align: center; letter-spacing: 1px; }
  .tab-active { background: var(--teal); }
  .tab-idle { background: var(--slate); border: 2px solid var(--teal); border-bottom: none; color: #e9f1f4; }
  .service-panel { position: absolute; left: 206px; top: 215px; width: 790px; height: 558px; background: var(--teal); }
  .divider-v { position: absolute; top: 20px; bottom: 20px; border-left: 2px dotted rgba(255,255,255,0.8); }
  .divider-h { position: absolute; left: 20px; right: 20px; top: 283px; border-top: 2px dotted rgba(255,255,255,0.8); }
  .service { position: absolute; width: 263px; text-align: center; }
  .service .ring { width: 100px; height: 100px; margin: 0 auto; border: 2px solid var(--white); border-radius: 50%; display: flex; align-items: center; justify-content: center; }
  .service h3 { margin-top: 12px; font-family: var(--heading); font-weight: 700; font-size: 17px; }
  .service p { margin-top: 6px; font-size: 12px; line-height: 16px; padding: 0 50px; }

  /* Contact */
  .contact { height: 625px; background: var(--orange); padding-top: 46px; }
  .contact-form { position: absolute; left: 248px; top: 171px; width: 704px; }
  .field { position: absolute; height: 44px; background: var(--white); color: #555; font-size: 12px; padding: 14px 18px; }
  .field-name { left: 0; top: 0; width: 339px; }
  .field-email { left: 365px; top: 0; width: 339px; }
  .field-message { left: 0; top: 67px; width: 704px; height: 160px; }
  .btn-send { position: absolute; left: 286px; top: 280px; width: 132px; height: 44px; background: var(--white); color: var(--ink); font-size: 15px; font-weight: 600; letter-spacing: 2px; line-height: 44px; text-align: center; }
  .social-links { position: absolute; top: 544px; left: 0; width: 1200px; display: flex; justify-content: center; gap: 46px; list-style: none; font-size: 17px; font-weight: 600; }

  /* Footer */
  .site-footer { height: 345px; background: var(--navy); padding-top: 80px; text-align: center; }
  .footer-brand { font-family: var(--hero); font-weight: 700; font-size: 34px; letter-spacing: 2px; }
  .footer-text { margin-top: 14px; font-size: 13px; line-height: 20px; }
  .footer-dots { margin-top: 68px; display: flex; justify-content: center; gap: 32px; }
  .footer-dots span { width: 42px; height: 42px; border: 2px solid var(--white); border-radius: 50%; }
</style>
</head>
<body>

<header class="hero">
  <div class="hero-photo" role="img" aria-label="Blurred photo of business people at an office meeting"></div>
  <div class="hero-shade"></div>
  <nav class="site-nav">
    <div class="brand">LOGO</div>
    <ul class="nav-links">
      <li>HOME</li><li>ABOUT</li><li>WORK</li><li>SERVICES</li><li>TEAM</li><li>CONTACT</li>
    </ul>
  </nav>
  <div class="hero-copy">
    <h1 class="hero-title">Finally, <strong>SEO services</strong><br>that actually work.</h1>
    <p class="hero-lead">Top-notch SEO services that are guaranteed to boost your<br>search engine rankings. 100% Searchly-friendly.</p>
  </div>
  <div class="btn-outline">Learn More</div>
</header>

<section class="why">
  <h2 class="section-title">WHY CHOOSE <strong>RANKLOFT</strong></h2>
  <p class="section-sub">Fusce dapibus, tellus ac cursus commodo, tortor mauris condimentum.<br>Duis mollis, est non commodo luctus, nisi erat porttitor ligula, eget lacinia odio sem nec elit.</p>
  <svg class="arrow arrow-left" width="30" height="90" viewBox="0 0 30 90"><polyline points="28,2 2,45 28,88" fill="none" stroke="#fff" stroke-width="2"/></svg>
  <svg class="arrow arrow-right" width="30" height="90" viewBox="0 0 30 90"><polyline points="2,2 28,45 2,88" fill="none" stroke="#fff" stroke-width="2"/></svg>
  <div class="features">
    <div class="feature" style="left:237px">
      <svg width="60" height="72" viewBox="0 0 60 72"><path d="M8 2h44v68L30 54 8 70z" fill="none" stroke="#fff" stroke-width="3"/><line x1="18" y1="18" x2="42" y2="18" stroke="#fff" stroke-width="3"/><line x1="18" y1="28" x2="42" y2="28" stroke="#fff" stroke-width="3"/></svg>
      <h3>BRANDING</h3>
      <p>Lorem ipsum dolor sit amet, consectetuer adipiscing elit, sed diam nonummy nibh.</p>
    </div>
    <div class="feature" style="left:478px">
      <svg width="72" height="72" viewBox="0 0 72 72"><path d="M52 6l14 14L24 62 6 66l4-18z" fill="none" stroke="#fff" stroke-width="3" stroke-linejoin="round"/><line x1="44" y1="14" x2="58" y2="28" stroke="#fff" stroke-width="3"/><line x1="10" y1="48" x2="24" y2="62" stroke="#fff" stroke-width="3"/></svg>
      <h3>DESIGN</h3>
      <p>Sed ut perspiciatis unde omnis iste natus error sit voluptatem.</p>
    </div>
    <div class="feature" style="left:726px">
      <svg width="76" height="72" viewBox="0 0 76 72"><rect x="3" y="6" width="70" height="46" fill="none" stroke="#fff" stroke-width="3"/><line x1="38" y1="52" x2="38" y2="64" stroke="#fff" stroke-width="3"/><line x1="24" y1="66" x2="52" y2="66" stroke="#fff" stroke-width="3"/></svg>
      <h3>DEVELOPMENT</h3>
      <p>At vero eos et accusamus et iusto odio dignissimos qui blanditiis praesentium.</p>
    </div>
  </div>
</section>

<section class="plans">
  <h2 class="section-title">SELECT A <strong>BOOSTER PLAN</strong></h2>
  <p class="section-sub">Neque porro quisquam est, qui dolorem ipsum quia dolor sit amet.</p>
  <div class="plan-table">
    <div class="plan">
      <div class="plan-head"><div class="plan-name">PERSONAL</div><div class="plan-price">$9/Month</div></div>
      <ul class="plan-list"><li>Free feature one</li><li>Unlimited feature two</li><li>Unlimited feature three</li><li>2x feature four</li><li>100x feature five</li></ul>
      <div class="plan-btn">GET STARTED</div>
    </div>
    <div class="plan">
      <div class="plan-head"><div class="plan-name">PROFESSIONAL</div><div class="plan-price">$14/Month</div></div>
      <ul class="plan-list"><li>Free feature one</li><li>Unlimited feature two</li><li>Unlimited feature three</li><li>2x feature four</li><li>100x feature five</li></ul>
      <div class="plan-btn">GET STARTED</div>
    </div>
    <div class="plan plan-featured">
      <div class="plan-head"><div class="plan-name">BUSINESS</div><div class="plan-price">$24/Month</div></div>
      <ul class="plan-list"><li>Free feature one</li><li>Unlimited feature two</li><li>Unlimited feature three</li><li>2x feature four</li><li>100x feature five</li></ul>
      <div class="plan-btn">GET STARTED</div>
    </div>
    <div class="plan">
      <div class="plan-head"><div class="plan-name">ENTERPRISE</div><div class="plan-price">$45/Month</div></div>
      <ul class="plan-list"><li>Free feature one</li><li>Unlimited feature two</li><li>Unlimited feature three</li><li>2x feature four</li><li>100x feature five</li></ul>
      <div class="plan-btn">GET STARTED</div>
    </div>
  </div>
</section>

<section class="guarantee">
  <p class="guarantee-text">30-DAY MONEY-BACK <strong>GUARANTEE</strong></p>
  <div class="btn-navy">LERAN MORE</div>
</section>

<section class="services">
  <h2 class="section-title">SEO <strong>SERVICES</strong></h2>
  <p class="section-sub">Fusce dapibus, tellus ac cursus commodo, tortor mauris condimentum.<br>Duis mollis, est non commodo luctus, nisi erat porttitor ligula, eget lacinia odio sem nec elit.</p>
  <div class="tabs">
    <div class="tab tab-active">INDIVIDUAL</div>
    <div class="tab tab-idle">SOCIAL MEDIA</div>
  </div>
  <div class="service-panel">
    <div class="divider-v" style="left:257px"></div>
    <div class="divider-v" style="left:531px"></div>
    <div class="divider-h"></div>

    <div class="service" style="left:0;top:30px">
      <div class="ring"><svg width="48" height="40" viewBox="0 0 48 40"><path d="M2 10h10l20 20h12M2 30h10l20-20h12" fill="none" stroke="#fff" stroke-width="3"/><polyline points="38,4 44,10 38,16" fill="none" stroke="#fff" stroke-width="3"/><polyline points="38,24 44,30 38,36" fill="none" stroke="#fff" stroke-width="3"/></svg></div>
      <h3>BRANDING</h3>
      <p>Lorem ipsum dolor sit amet, consectetuer adipiscing elit, sed diam nonummy nibh.</p>
    </div>
    <div class="service" style="left:263px;top:30px">
      <div class="ring"><svg width="48" height="40" viewBox="0 0 48 40"><path d="M6 22V10h36" fill="none" stroke="#fff" stroke-width="3"/><polyline points="36,4 42,10 36,16" fill="none" stroke="#fff" stroke-width="3"/><path d="M42 18v12H6" fill="none" stroke="#fff" stroke-width="3"/><polyline points="12,24 6,30 12,36" fill="none" stroke="#fff" stroke-width="3"/></svg></div>
      <h3>DESIGN</h3>
      <p>Sed ut perspiciatis unde omnis iste natus error sit voluptatem.</p>
    </div>
    <div class="service" style="left:527px;top:30px">
      <div class="ring"><svg width="44" height="40" viewBox="0 0 44 40"><rect x="3" y="6" width="38" height="30" rx="3" fill="none" stroke="#fff" stroke-width="3"/><rect x="24" y="15" width="17" height="12" fill="none" stroke="#fff" stroke-width="3"/><circle cx="30" cy="21" r="2" fill="#fff"/></svg></div>
      <h3>DEVELOPMENT</h3>
      <p>At vero eos et accusamus et iusto odio dignissimos qui blanditiis praesentium.</p>
    </div>

    <div class="service" style="left:0;top:320px">
      <div class="ring"><svg width="48" height="40" viewBox="0 0 48 40"><path d="M2 10h10l20 20h12M2 30h10l20-20h12" fill="none" stroke="#fff" stroke-width="3"/><polyline points="38,4 44,10 38,16" fill="none" stroke="#fff" stroke-width="3"/><polyline points="38,24 44,30 38,36" fill="none" stroke="#fff" stroke-width="3"/></svg></div>
      <h3>BRANDING</h3>
      <p>Lorem ipsum dolor sit amet, consectetuer adipiscing elit, sed diam nonummy nibh.</p>
    </div>
    <div class="service" style="left:263px;top:320px">
      <div class="ring"><svg width="48" height="40" viewBox="0 0 48 40"><path d="M6 22V10h36" fill="none" stroke="#fff" stroke-width="3"/><polyline points="36,4 42,10 36,16" fill="none" stroke="#fff" stroke-width="3"/><path d="M42 18v12H6" fill="none" stroke="#fff" stroke-width="3"/><polyline points="12,24 6,30 12,36" fill="none" stroke="#fff" stroke-width="3"/></svg></div>
      <h3>DESIGN</h3>
      <p>Sed ut perspiciatis unde omnis iste natus error sit voluptatem.</p>
    </div>
    <div class="service" style="left:527px;top:320px">
      <div class="ring"><svg width="44" height="40" viewBox="0 0 44 40"><rect x="3" y="6" width="38" height="30" rx="3" fill="none" stroke="#fff" stroke-width="3"/><rect x="24" y="15" width="17" height="12" fill="none" stroke="#fff" stroke-width="3"/><circle cx="30" cy="21" r="2" fill="#fff"/></svg></div>
      <h3>DEVELOPMENT</h3>
      <p>At vero eos et accusamus et iusto odio dignissimos qui blanditiis praesentium.</p>
    </div>
  </div>
</section>

<section class="contact">
  <h2 class="section-title">GET IN <strong>TOUCH</strong></h2>
  <p class="section-sub">48 Harrow Lane, Brightwater, BW 40212. Tel: (555) 014-2876</p>
  <div class="contact-form">
    <div class="field field-name">Your Name</div>
    <div class="field field-email">Your Email</div>
    <div class="field field-message">Your Message</div>
    <div class="btn-send">SEND</div>
  </div>
  <ul class="social-links">
    <li>Friendwall</li><li>Chirper</li><li>Circlesy</li><li>Linkwork</li>
  </ul>
</section>

<footer class="site-footer">
  <div class="footer-brand">LOGO</div>
  <p class="footer-text">Fusce dapibus, tellus ac cursus commodo, tortor mauris condimentum.<br>Duis mollis, est non commodo luctus, nisi erat porttitor ligula.</p>
  <div class="footer-dots"><span></span><span></span><span></span></div>
</footer>

</body>
</html>
```